We need a new website design for our company Brindle Forks (https://www.brindleforks.example/). We DO NOT WANT A BORING STANDARD SITE. This site has to be different, and has to POP!

Logo Files: https://files.example-share.net/folders/7kQwT2mZpL9xR4vB8nJc3HdYs6uFa1oE

Website Photos here: https://files.example-share.net/folders/5R-GhuK2W_pqtVnaLiEy47zmkTd83bv

Websites we like:
https://morrowind-demo.sitecraft.example/
http://plattero.example/

We will need the site building Wordpress/Woocommerce and also help with interior pages & installation plug-ins -- see further attachments.

Information about the company:
1. PURPOSE: Why do we exist?
We believe that food is the root source to healthy living.
2. VISION: What future do we want to help create?
A world of healthy and happy people.
3. MISSION: What are we here to do?
Empower every person to utilize food as a means of living a healthy life.

Value Proposition:
Brindle Forks develops new food based on the latest science to provide the human body with the proper nutrients for optimal health. Our research based foods target the key health functions that support healthy aging and active lifestyles. Since 2002, we have been innovating and designing our meals to meet the needs for healthy aging to active lifestyles. To help people perform their best, today & in the future.

Objective:
This is a nationwide issue and it's coming to the surface. Food affects people in a number of different ways. Our objective is to create an approachable and sustainable solution that can assist people with a number of ailments. The end result for all of them is feeling a feeling they haven't felt in quite some time. Feeling a refreshed you. Like water for fish, food for humans. Keep it clean and simple so you can focus on enjoying your life.

PHRASES/TAGLINES:
Empowerment Through Food
Real Food, Real Results
Nutrition Made Simple
Not Just Meal Prep, Food Science
A healthier you, delivered to your door
Increase your health and wellness baseline.
Discover the potential of healthier eating
Become the best version of you
It’s incredible what proper nutrition feels like
Taste & feel the difference. Your future self will thank you.
A healthier you is just a meal away
Life Changing results
Overwhelmed with being healthy, stops here.
Designed by doctors, approved by humans
Results Driven Healthy Eating, Delivered to you.
Become the person you deserve to be.
Enjoy the process of becoming a better you

Value Propositions:
We Educate & Empower People Through Food to Live Their Best Life
Sustainable health through proper nutrition… that’s enjoyable too.

Key Statements:
We provide satisfying meals that are nutrient dense & deliver results.
Our meals provide an easy way to enjoy an anti-inflammatory diet that's as satisfying as it is healthy.
Health, fat loss & feeling good through chef-prepared, nutrient-dense, satisfying meals delivered to your door.

PLEASE REVIEW THE ATTACHMENTS.

Industry/Entity Type

See Description & Attachments

Coding

Coded - Design and coding required

Number of Pages Required

5+ page

Font styles to use
Other font styles liked:
• See Description & Attachments

Colors
0094D4
00A9DD
6FCCEA
C7EBF8
E9F6FB
00AB8E
00BBA5
67D7C9
C6EFE9
E9F9F6

Requirements
Must have
Nice to have
Should not have

```html
<!DOCTYPE html>
<html lang="en">
<head>
<meta charset="utf-8">
<title>Brindle Forks — Real Food, Real Results</title>
<link rel="stylesheet" href="https://fonts.googleapis.com/css2?family=Josefin+Sans:wght@400;600;700&family=Raleway:wght@400;500;600;700&display=swap">
<style>
:root{
  --green-dark:#155437;
  --green-deep:#0f5236;
  --green-sage:#b9cfae;
  --green-mist:#e4eee0;
  --ink:#1d1d1b;
  --grey:#6b6b6b;
  --footer:#262a27;
  --white:#ffffff;
  --head:"Josefin Sans",sans-serif;
  --body:"Raleway",sans-serif;
}
*{box-sizing:border-box;margin:0;padding:0}
html,body{width:1200px;height:4873px;overflow:hidden}
body{position:relative;background:var(--white);font-family:var(--body);color:var(--ink)}
.abs{position:absolute}
.backdrop{position:absolute;left:0;top:0;width:1200px;height:4873px}
.btn{position:absolute;display:flex;align-items:center;justify-content:center;background:var(--green-dark);color:var(--white);border-radius:24px;font-family:var(--body);font-weight:700;font-size:15px;letter-spacing:.5px;text-transform:uppercase}
.btn-outline{background:transparent;color:var(--green-dark);border:2px solid var(--green-dark)}

/* header */
.brand{position:absolute;left:98px;top:48px;font-family:var(--head);font-weight:700;font-size:32px;color:var(--green-dark);display:flex;align-items:center;gap:10px}
.brand-dot{width:16px;height:16px;border-radius:50%;background:var(--green-dark)}
.brand-tag{position:absolute;left:98px;top:132px;font-size:11px;letter-spacing:2.5px;font-weight:700;color:var(--green-dark)}
.nav{position:absolute;top:34px;font-size:15px;font-weight:500;color:var(--ink)}
.nav-home{color:var(--green-dark);font-weight:600}
.login{left:962px;top:25px;width:138px;height:45px;font-size:17px}

/* hero */
.hero-title{position:absolute;left:95px;top:222px;font-family:var(--head);font-weight:700;font-size:76px;line-height:78px;color:var(--ink)}
.shop-now{left:98px;top:409px;width:156px;height:49px}
.plate{position:absolute;left:579px;top:108px;width:522px;height:522px;border-radius:50%;background:radial-gradient(circle at 40% 35%,#ffffff 55%,#dedfe4 100%);box-shadow:0 18px 30px rgba(0,0,0,.15)}
.plate-food{position:absolute;left:96px;top:90px;width:330px;height:330px;border-radius:50%;background:radial-gradient(circle at 45% 45%,#f2c13a 0%,#e79a2c 45%,#c9731f 80%,#8aa54b 100%)}

/* values */
.value{position:absolute;width:300px;text-align:center}
.value-icon{display:block;margin:0 auto}
.value h3{margin-top:22px;font-family:var(--body);font-weight:600;font-size:20px;letter-spacing:.5px;color:var(--ink)}
.value p{margin-top:10px;font-size:15px;line-height:24px;color:var(--grey)}

/* about */
.about-title{position:absolute;left:98px;top:1236px;font-family:var(--head);font-weight:700;font-size:46px;color:var(--ink)}
.about-sub{position:absolute;left:98px;top:1298px;font-family:var(--head);font-weight:600;font-size:21px;letter-spacing:.5px}
.about-text{position:absolute;left:98px;top:1345px;width:480px;font-size:15px;line-height:24.3px;color:#333}
.read-more{left:98px;top:1510px;width:156px;height:46px}
.bowl{position:absolute;left:598px;top:1141px;width:538px;height:538px;border-radius:50%;background:radial-gradient(circle at 50% 50%,#2b2f4a 60%,#1b1e33 100%);box-shadow:-20px 30px 40px rgba(0,0,0,.25)}
.bowl-food{position:absolute;left:94px;top:94px;width:350px;height:350px;border-radius:50%;background:radial-gradient(circle at 48% 52%,#d8553a 0%,#c9452d 40%,#f0efe6 62%,#4f8a34 85%,#2b2f4a 100%)}

/* menu */
.section-title{position:absolute;left:0;width:1200px;text-align:center;font-family:var(--head);font-weight:700;color:var(--ink)}
.menu-card{position:absolute;width:242px;height:372px}
.menu-photo{width:242px;height:175px;border-radius:4px}
.menu-card h4{margin-top:16px;font-family:var(--head);font-weight:700;font-size:20px;line-height:24px;letter-spacing:.3px}
.menu-info{margin-top:6px;font-size:13.5px;line-height:23px;color:var(--grey)}
.price{margin-top:4px;font-size:14px;font-weight:700}
.add{left:0;bottom:0;width:140px;height:42px;font-size:12px}
.load-more{left:515px;top:2715px;width:170px;height:45px}

/* faq */
.faq-list{position:absolute;left:240px;top:2985px;width:722px}
.faq-item{height:44px;margin-bottom:12px;background:var(--green-dark);color:var(--white);display:flex;align-items:center;justify-content:space-between;padding:0 16px 0 17px;font-size:17px;font-weight:600}
.view-all{left:515px;top:3277px;width:170px;height:45px}

/* audience */
.aud-title{position:absolute;left:98px;top:3552px;font-family:var(--head);font-weight:700;font-size:46px;color:var(--white)}
.aud-card{position:absolute;top:3659px;width:316px;height:203px;border:1.5px solid rgba(255,255,255,.8);border-radius:12px;padding:18px 16px 0 130px;color:var(--white)}
.aud-photo{position:absolute;left:14px;top:34px;width:102px;height:102px;border-radius:50%;border:3px solid #1d2b3a}
.aud-card h4{font-size:17px;font-weight:700;margin-bottom:6px}
.aud-card p{font-size:14px;line-height:21px}

/* stats */
.stat{position:absolute;top:4178px;width:280px;text-align:center}
.stat svg{display:block;margin:0 auto}
.stat-num{margin-top:24px;font-family:var(--head);font-weight:700;font-size:44px;line-height:44px}
.stat-label{margin-top:6px;font-size:17px;letter-spacing:.3px;color:#333}

/* footer */
.foot-col{position:absolute;top:4528px;color:#d9d9d9}
.foot-col h5{font-size:14px;letter-spacing:1px;font-weight:700;color:#e0e0e0;margin-bottom:20px}
.foot-col li{list-style:none;font-size:14px;line-height:34.5px}
.foot-col li::before{content:"›";margin-right:10px;font-size:17px}
.newsletter{position:absolute;left:789px;top:4568px;width:311px;height:52px;border-radius:26px;background:var(--white);display:flex;align-items:center;justify-content:space-between;padding:0 22px 0 14px;font-size:14px;color:#555}
.foot-rule{position:absolute;left:100px;top:4806px;width:1000px;height:1px;background:#555}
.copyright{position:absolute;left:100px;top:4832px;font-size:13px;color:#ddd}
.copyright b{color:#fff}
.pay{position:absolute;top:4830px;width:40px;height:26px;border-radius:3px;background:#e6e6e6}
</style>
</head>
<body>

<svg class="backdrop" viewBox="0 0 1200 4873" aria-hidden="true">
  <!-- hero brush band -->
  <path fill="#b9cfae" d="M560 0H1098L1102 40 1094 90 1100 160 1092 240 1099 320 1090 400 1096 470 1080 548 1000 540 900 548 820 536 720 546 640 538 556 545 560 470 551 400 558 300 548 220 556 140 550 60Z"/>
  <!-- about band -->
  <path fill="#e4eee0" d="M0 1130C200 1100 420 1140 640 1120S1000 1100 1200 1120V1620C1000 1650 780 1610 560 1640S180 1660 0 1640Z"/>
  <circle cx="4" cy="1238" r="20" fill="none" stroke="#155437" stroke-width="6"/>
  <circle cx="575" cy="1220" r="8" fill="none" stroke="#155437" stroke-width="3"/>
  <circle cx="1132" cy="1590" r="5" fill="none" stroke="#155437" stroke-width="2"/>
  <!-- faq band -->
  <path fill="#e4eee0" d="M0 2815C260 2845 520 2825 780 2835S1060 2845 1200 2825V3440H0Z"/>
  <circle cx="1180" cy="2965" r="26" fill="none" stroke="#155437" stroke-width="7"/>
  <!-- audience band -->
  <path fill="#0f5236" d="M0 3440C120 3420 260 3400 420 3412S800 3445 1000 3430 1140 3410 1200 3415V3955C1000 3975 760 3950 520 3965S160 3985 0 3965Z"/>
  <path fill="none" stroke="#155437" stroke-width="7" d="M164 3425A20 20 0 0 1 204 3425"/>
  <!-- footer -->
  <path fill="#262a27" d="M0 4415C160 4440 340 4450 520 4430S900 4395 1200 4425V4873H0Z"/>
</svg>

<header>
  <div class="brand"><span class="brand-dot"></span>Brindle Forks</div>
  <div class="brand-tag">EAT BETTER. LIVE BETTER.</div>
  <span class="nav nav-home" style="left:318px">Home</span>
  <span class="nav" style="left:394px">Shop Now</span>
  <span class="nav" style="left:500px">About</span>
  <span class="nav" style="left:577px">Menu</span>
  <span class="nav" style="left:649px">Programs</span>
  <span class="nav" style="left:751px">FAQ</span>
  <svg class="abs" style="left:880px;top:34px" width="18" height="16" viewBox="0 0 18 16"><path d="M0 1h3l2 9h10l2-7H5" fill="none" stroke="#1d1d1b" stroke-width="2"/><circle cx="6" cy="14" r="1.6" fill="#1d1d1b"/><circle cx="14" cy="14" r="1.6" fill="#1d1d1b"/></svg>
  <svg class="abs" style="left:928px;top:34px" width="16" height="16" viewBox="0 0 16 16"><circle cx="6.5" cy="6.5" r="5" fill="none" stroke="#1d1d1b" stroke-width="2"/><path d="M10 10l5 5" stroke="#1d1d1b" stroke-width="2.4"/></svg>
  <span class="btn login">Login</span>
</header>

<section class="hero">
  <h1 class="hero-title">Real Food,<br>Real Results</h1>
  <span class="btn shop-now">Shop Now</span>
  <svg class="abs" style="left:103px;top:568px" width="22" height="32" viewBox="0 0 22 32"><rect x="2" y="2" width="18" height="28" rx="9" fill="none" stroke="#1d1d1b" stroke-width="2.5"/><rect x="10" y="7" width="2.5" height="6" rx="1" fill="#1d1d1b"/></svg>
  <div class="plate"><div class="plate-food" role="img" aria-label="Roasted sweet potato, cauliflower, peas and rice bowl"></div></div>
</section>

<section class="values">
  <div class="value" style="left:90px;top:776px">
    <svg class="value-icon" width="160" height="108" viewBox="0 0 160 108"><path d="M20 70C10 30 60 0 110 6S160 60 150 90 60 110 20 70Z" fill="#155437"/><circle cx="82" cy="50" r="26" fill="#fff"/><circle cx="82" cy="50" r="18" fill="#e53935"/><circle cx="82" cy="50" r="10" fill="#fff"/><circle cx="82" cy="50" r="5" fill="#e53935"/><circle cx="104" cy="72" r="9" fill="#6ec33f"/><path d="M99 72l4 4 6-7" fill="none" stroke="#fff" stroke-width="2.5"/></svg>
    <h3>PURPOSE</h3>
    <p>We believe that food is the root<br>source to healthy living.</p>
  </div>
  <div class="value" style="left:450px;top:776px">
    <svg class="value-icon" width="160" height="108" viewBox="0 0 160 108"><path d="M20 70C10 30 60 0 110 6S160 60 150 90 60 110 20 70Z" fill="#155437"/><circle cx="84" cy="46" r="22" fill="#5aa9e6"/><circle cx="84" cy="44" r="12" fill="#f7c948"/><rect x="77" y="58" width="14" height="10" rx="2" fill="#d9d9d9"/><path d="M60 24l-6-6M108 24l6-6M84 16V6" stroke="#f7c948" stroke-width="3"/></svg>
    <h3>VISION</h3>
    <p>A world of healthy and happy<br>people.</p>
  </div>
  <div class="value" style="left:810px;top:776px">
    <svg class="value-icon" width="160" height="108" viewBox="0 0 160 108"><path d="M20 70C10 30 60 0 110 6S160 60 150 90 60 110 20 70Z" fill="#155437"/><rect x="70" y="28" width="4" height="52" fill="#6b4a2b"/><path d="M74 30h34l-8 12 8 12H74Z" fill="#f7b500"/></svg>
    <h3>MISSION</h3>
    <p>Empower every person to utilize food<br>as a means of living a healthy life.</p>
  </div>
</section>

<section class="about">
  <h2 class="about-title">About</h2>
  <div class="about-sub">Value Proposition</div>
  <p class="about-text">Brindle Forks develops new food based on the latest science to provide the human body with the proper nutrients for optimal health. Our research based foods target the key health functions that support healthy aging and active lifestyles. Since 2002, we have been innovating and designing our meals to meet the needs for healthy aging to active lifestyles.</p>
  <span class="btn read-more">Read More</span>
  <div class="bowl"><div class="bowl-food" role="img" aria-label="Ground turkey with cauliflower and fresh herbs in a dark bowl"></div></div>
</section>

<section class="menu">
  <h2 class="section-title" style="top:1792px;font-size:46px">Our Menu</h2>

  <div class="menu-card" style="left:98px;top:1864px">
    <div class="menu-photo" role="img" aria-label="Chicken quinoa bowl" style="background:linear-gradient(135deg,#c9ab7c,#8a7b56 55%,#d8d3c4)"></div>
    <h4>Chicken quinoa bowl</h4>
    <p class="menu-info">Cal 477 | gluten free | no antibiotics | no hormones | all natural</p>
    <p class="price">$13.00</p>
    <span class="btn add">Add to cart</span>
  </div>
  <div class="menu-card" style="left:352px;top:1864px">
    <div class="menu-photo" role="img" aria-label="Chocolate almond oats in jars" style="background:linear-gradient(135deg,#4a3b2c,#a58f6e 50%,#2f2a24)"></div>
    <h4>Chocolate almond oats</h4>
    <p class="menu-info">Cal 353 | gluten free | no antibiotics| no hormones | all natural</p>
    <p class="price">$ 6.50</p>
    <span class="btn add">Add to cart</span>
  </div>
  <div class="menu-card" style="left:606px;top:1864px">
    <div class="menu-photo" role="img" aria-label="Blueberry almond oats in jars" style="background:linear-gradient(135deg,#b6a283,#5d5a66 50%,#d7cbb5)"></div>
    <h4>Blueberry almond oats</h4>
    <p class="menu-info">Cal 331 | gluten free | no antibiotics | no hormones | all natural</p>
    <p class="price">$13.00</p>
    <span class="btn add">Add to cart</span>
  </div>
  <div class="menu-card" style="left:859px;top:1864px">
    <div class="menu-photo" role="img" aria-label="Chicken greek salad" style="background:linear-gradient(135deg,#3f6a2f,#d8c49e 50%,#7a2e2e)"></div>
    <h4>Chicken greek salad</h4>
    <p class="menu-info">Cal 312 | gluten free | no antibiotics | no hormones | all natural</p>
    <p class="price">$12.50</p>
    <span class="btn add">Add to cart</span>
  </div>

  <div class="menu-card" style="left:98px;top:2289px">
    <div class="menu-photo" role="img" aria-label="Spinach and feta stuffed chicken with broccoli" style="background:linear-gradient(135deg,#4a6b2a,#3a2e28 55%,#8aa55a)"></div>
    <h4>Spinach and feta<br>stuffed chicken</h4>
    <p class="menu-info">Cal 611 | gluten free | no antibiotics no hormones | all natural</p>
    <p class="price">$13.00</p>
    <span class="btn add">Add to cart</span>
  </div>
  <div class="menu-card" style="left:352px;top:2289px">
    <div class="menu-photo" role="img" aria-label="Chicken blueberry goat cheese salad" style="background:linear-gradient(135deg,#355a2a,#c8b89a 50%,#2f3a22)"></div>
    <h4>Chicken blueberry<br>goat cheese salad</h4>
    <p class="menu-info">Cal 296 | gluten free | low carb antioxidant rich</p>
    <p class="price">$13.00</p>
    <span class="btn add">Add to cart</span>
  </div>
  <div class="menu-card" style="left:606px;top:2289px">
    <div class="menu-photo" role="img" aria-label="Mediterranean tuna with tomatoes" style="background:linear-gradient(135deg,#e3c9b0,#d7b49a 50%,#c83a2a)"></div>
    <h4>Mediterranean tuna</h4>
    <p class="menu-info">Cal 177 | gluten free | low carb low calorie</p>
    <p class="price">$13.00</p>
    <span class="btn add">Add to cart</span>
  </div>
  <div class="menu-card" style="left:859px;top:2289px">
    <div class="menu-photo" role="img" aria-label="Turkey tips with roasted vegetables" style="background:linear-gradient(135deg,#9a4a24,#c9812f 45%,#4f7a2c)"></div>
    <h4>Turkey Tips</h4>
    <p class="menu-info">Cal 283 | paleo | low carb | keto gluten free</p>
    <p class="price">$12.50</p>
    <span class="btn add">Add to cart</span>
  </div>

  <span class="btn btn-outline load-more">Load More</span>
</section>

<section class="faq">
  <h2 class="section-title" style="top:2912px;font-size:50px">Frequently Asked Questions</h2>
  <div class="faq-list">
    <div class="faq-item"><span>Q. What is Brindle Forks?</span><svg width="20" height="20" viewBox="0 0 20 20"><circle cx="10" cy="10" r="10" fill="#fff"/><path d="M8 5l5 5-5 5" fill="none" stroke="#155437" stroke-width="2.4"/></svg></div>
    <div class="faq-item"><span>Q. Can I customize my order?</span><svg width="20" height="20" viewBox="0 0 20 20"><circle cx="10" cy="10" r="10" fill="#fff"/><path d="M8 5l5 5-5 5" fill="none" stroke="#155437" stroke-width="2.4"/></svg></div>
    <div class="faq-item"><span>Q. Do you have gluten free options?</span><svg width="20" height="20" viewBox="0 0 20 20"><circle cx="10" cy="10" r="10" fill="#fff"/><path d="M8 5l5 5-5 5" fill="none" stroke="#155437" stroke-width="2.4"/></svg></div>
    <div class="faq-item"><span>Q. Why pre-order online?</span><svg width="20" height="20" viewBox="0 0 20 20"><circle cx="10" cy="10" r="10" fill="#fff"/><path d="M8 5l5 5-5 5" fill="none" stroke="#155437" stroke-width="2.4"/></svg></div>
    <div class="faq-item"><span>Q. What is the window for ordering?</span><svg width="20" height="20" viewBox="0 0 20 20"><circle cx="10" cy="10" r="10" fill="#fff"/><path d="M8 5l5 5-5 5" fill="none" stroke="#155437" stroke-width="2.4"/></svg></div>
  </div>
  <span class="btn btn-outline view-all">View All</span>
</section>

<section class="audience">
  <h2 class="aud-title">Who is Brindle Forks For?</h2>
  <svg class="abs" style="left:1019px;top:3554px" width="38" height="38" viewBox="0 0 38 38"><circle cx="19" cy="19" r="17" fill="none" stroke="#cfe3c6" stroke-width="2"/><path d="M22 11l-8 8 8 8" fill="none" stroke="#cfe3c6" stroke-width="2.5"/></svg>
  <svg class="abs" style="left:1064px;top:3554px" width="38" height="38" viewBox="0 0 38 38"><circle cx="19" cy="19" r="18" fill="#b9cfae"/><path d="M16 11l8 8-8 8" fill="none" stroke="#155437" stroke-width="2.5"/></svg>

  <div class="aud-card" style="left:98px">
    <div class="aud-photo" role="img" aria-label="Meal prep container with roasted vegetables" style="background:radial-gradient(circle,#e0962f,#b8562a 60%,#23303f)"></div>
    <h4>General Health</h4>
    <p>You need the support of a healthy diet to get back in shape and improve your overall health. Having a meal plan that supports you would benefit you.</p>
  </div>
  <div class="aud-card" style="left:441px">
    <div class="aud-photo" role="img" aria-label="Bowl of turkey with greens" style="background:radial-gradient(circle,#d14a30,#5a8a34 60%,#23303f)"></div>
    <h4>Business Individuals</h4>
    <p>You have a growing to-do list that never seems to end. No time to do healthy meal prep. You prefer a healthy meal over a fast food diet.</p>
  </div>
  <div class="aud-card" style="left:784px">
    <div class="aud-photo" role="img" aria-label="Colourful vegetable meal box" style="border-radius:10px;background:linear-gradient(135deg,#e2a23a,#6b2c5a 50%,#4a8a2e)"></div>
    <h4>Fitness Enthusiasts</h4>
    <p>You eat clean, fitness &amp; eating right are a huge part of your life. Enjoy healthy meal delivery to keep yourself on track.</p>
  </div>
</section>

<section class="stats">
  <h2 class="section-title" style="top:4066px;font-size:50px">Award Winning Meals</h2>
  <div class="stat" style="left:27px">
    <svg width="62" height="62" viewBox="0 0 62 62" role="img" aria-label="Happy clients icon"><circle cx="31" cy="31" r="29" fill="#f7c948" stroke="#1d1d1b" stroke-width="2"/></svg>
    <div class="stat-num">150K</div><div class="stat-label">HAPPY CLIENTS</div>
  </div>
  <div class="stat" style="left:324px">
    <svg width="70" height="62" viewBox="0 0 70 62" role="img" aria-label="Serving cloche icon"><path d="M10 40a25 25 0 0 1 50 0Z" fill="#f7b500" stroke="#1d1d1b" stroke-width="2"/><rect x="6" y="40" width="58" height="5" rx="2" fill="#1d1d1b"/><circle cx="35" cy="12" r="4" fill="#1d1d1b"/><path d="M20 50h30l-6 8H26Z" fill="#f7b500" stroke="#1d1d1b" stroke-width="2"/></svg>
    <div class="stat-num">500K</div><div class="stat-label">MEALS SERVED NATION WIDE</div>
  </div>
  <div class="stat" style="left:653px">
    <svg width="62" height="62" viewBox="0 0 62 62" role="img" aria-label="Chef prepared meals icon"><rect x="12" y="4" width="38" height="18" rx="9" fill="#fff" stroke="#1d1d1b" stroke-width="2"/><rect x="18" y="22" width="26" height="8" fill="#fff" stroke="#1d1d1b" stroke-width="2"/><rect x="14" y="36" width="34" height="24" rx="6" fill="#f2f2f2" stroke="#1d1d1b" stroke-width="2"/></svg>
    <div class="stat-num">35+</div><div class="stat-label">CHEF PREPARED MEALS</div>
  </div>
  <div class="stat" style="left:894px">
    <svg width="62" height="62" viewBox="0 0 62 62" role="img" aria-label="Trophy icon"><path d="M16 4h30v16a15 15 0 0 1-30 0Z" fill="#f7b500" stroke="#1d1d1b" stroke-width="2"/><path d="M16 10H6c0 10 6 14 10 14M46 10h10c0 10-6 14-10 14" fill="none" stroke="#1d1d1b" stroke-width="2"/><rect x="28" y="35" width="6" height="12" fill="#f7b500" stroke="#1d1d1b" stroke-width="2"/><rect x="18" y="47" width="26" height="10" fill="#1d1d1b"/></svg>
    <div class="stat-num">215</div><div class="stat-label">AWARDS</div>
  </div>
</section>

<footer>
  <div class="foot-col" style="left:100px"><h5>MY ACCOUNT</h5><ul><li>Site Help</li><li>About Us</li><li>Contact Us</li><li>Shipping &amp; Returns</li><li>All Products</li><li>Gift Certificates</li></ul></div>
  <div class="foot-col" style="left:341px"><h5>VIEW CART</h5><ul><li>About Us</li><li>Corporate Catering</li><li>Podcast</li><li>Become an Affiliate</li></ul></div>
  <div class="foot-col" style="left:581px"><h5>ORDER STATUS</h5><ul><li>Contact Us</li><li>Privacy Policy</li><li>Testimonials</li></ul></div>
  <div class="foot-col" style="left:789px"><h5>STAY IN THE LOOP</h5></div>
  <div class="newsletter"><span>Enter email address</span><svg width="16" height="16" viewBox="0 0 16 16"><path d="M1 8l14-7-5 14-2-6Z" fill="#155437"/></svg></div>
  <div class="foot-rule"></div>
  <p class="copyright">© 2022 <b>Brindle Forks</b>. All right reserved</p>
  <span class="pay" style="left:899px"></span>
  <span class="pay" style="left:951px"></span>
  <span class="pay" style="left:1004px"></span>
  <span class="pay" style="left:1060px"></span>
</footer>

</body>
</html>
```